4th Generation Family Business Needs a New Card Design!

We are a family owned 4th Generation company. We are based in the Sydney, Australia area and we are desperately in need of a more modern and classy card. We are monumental masons who design, supply & erect lasting memorials throughout cemeteries in Sydney. Our customers are normally in a period of grieving. I have attached logo files that will need to be implemented on the card. Company was established 1935. Australian Owned and Operated. Card needs to be designed to PRINTLY.com specification.

Target Market(s)

Our target market is based upon people that a grieving for family members that have passed away. We also deal with alot of companies that own and operate cemeteries.

Industry/Entity Type

Business

Contact Information for Business Card

Oliver Brantley, Operations Manager, 0417552908, oliver@hollowaystoneworks.com.au
Martin Brantley, Director, 0431906627, martin@hollowaystoneworks.com.au
Phone # 02 9634 2258
Website: www.hollowaystoneworks.com.au
Address: Suite 17, 8 Calloway Lane, East Penrose, Sydney NSW 2290

Font styles to use
Serif
Decorative
Script

Requirements
Must have
• Would like to see the logo nicely implemented with a modern design. Embossed lettering would be a nice additive.

```html
<!DOCTYPE html>
<html lang="en">
<head>
<meta charset="utf-8">
<title>Holloway Stoneworks – Business Card</title>
<link rel="stylesheet" href="https://fonts.googleapis.com/css2?family=Open+Sans:wght@400;600;700;800&display=swap">
<style>
  :root {
    --backdrop: #e4e1dc;
    --card: #f4f2ee;
    --ink: #1c1c1c;
    --ink-soft: #2e2e2e;
    --gold: #f0c21f;
    --shadow: rgba(0,0,0,0.18);
  }
  * { margin: 0; padding: 0; box-sizing: border-box; }
  html, body {
    width: 909px; height: 1200px; overflow: hidden;
    background: var(--backdrop);
    font-family: "Open Sans", Arial, sans-serif;
    color: var(--ink);
  }
  .canvas {
    position: relative; width: 909px; height: 1200px;
  }
  .card {
    position: absolute; left: 75px; width: 760px; height: 465px;
    background: var(--card);
    box-shadow: 0 6px 18px var(--shadow);
  }
  .card--front { top: 62px; }
  .card--back { top: 673px; }

  .brand {
    position: absolute; left: 0; right: 0; top: 0; bottom: 0;
    display: flex; align-items: center; justify-content: center; gap: 14px;
  }
  .brand__mark {
    width: 22px; height: 22px; background: var(--gold);
  }
  .brand__name {
    font-weight: 700; font-size: 34px; letter-spacing: 3px;
    text-transform: uppercase; color: var(--ink);
  }

  .brand--small {
    left: 62px; top: auto; bottom: 110px; right: auto;
    justify-content: flex-start; gap: 8px;
  }
  .brand--small .brand__mark { width: 12px; height: 12px; }
  .brand--small .brand__name { font-size: 13px; letter-spacing: 1px; }

  .contact {
    position: absolute; left: 380px; top: 112px; width: 360px;
    font-size: 14.5px; line-height: 1.45; color: var(--ink-soft);
  }
  .contact__name {
    font-weight: 800; font-size: 24px; letter-spacing: 0.5px;
    text-transform: uppercase; color: var(--ink); line-height: 1.05;
  }
  .contact__role {
    font-weight: 700; font-size: 17px; color: var(--ink); margin-bottom: 22px;
  }
  .contact__group { margin-bottom: 20px; }
  .contact__label { font-weight: 700; color: var(--ink); }
</style>
</head>
<body>
<main class="canvas">
  <section class="card card--front" aria-label="Card front">
    <div class="brand">
      <span class="brand__mark"></span>
      <span class="brand__name">Holloway Stoneworks</span>
    </div>
  </section>

  <section class="card card--back" aria-label="Card back">
    <div class="brand brand--small">
      <span class="brand__mark"></span>
      <span class="brand__name">Holloway Stoneworks</span>
    </div>
    <div class="contact">
      <p class="contact__name">Oliver Brantley</p>
      <p class="contact__role">Operations Manager</p>
      <div class="contact__group">
        <p><span class="contact__label">Mobile.</span> 0417552908</p>
        <p>oliver@hollowaystoneworks.com.au</p>
      </div>
      <div class="contact__group">
        <p><span class="contact__label">Phone.</span> 02 9634 2258</p>
        <p>www.hollowaystoneworks.com.au</p>
      </div>
      <div class="contact__group">
        <p>Suite 17, 8 Calloway Lane</p>
        <p>East Penrose, Sydney NSW 2290</p>
      </div>
    </div>
  </section>
</main>
</body>
</html>
```